Harlan Ridge Smokehouse Jamboree's 10th ever event needs a Poster! This Non-Profit is a blast

We need a totally NEW and FUN poster design to promote our tiny Kentucky town which hosts 40,000+ people who come to meet the TV Celebrity BBQ Pitmasters - who smoke meat for their fans. It is all about Beers, Bands, BBQ + Bourbon. We are a family event with Free music all weekend long.

Target Market(s)

People who love Beer, BBQ, Bands and Bourbon

Colors
ec1f27
0555a3

Requirements
Must have
• Please only use original art.
• High energy / Fresh / Young
• Name: Harlan Ridge Smokehouse Jamboree
• 10th ever
• Sept 4+5, 2020
• Bands, Beer, BBQ + Bourbon
• Hosted by: Copperfield Hollow Distillery
• 2817 Marlow Pike Ashby, KY 40198
• $5 admission - FREE MUSIC - FREE Parking
Nice to have
• Please only use original art. Trademarked images and logos will be rejected.

```html
<!DOCTYPE html>
<html lang="en">
<head>
<meta charset="utf-8">
<title>Harlan Ridge Smokehouse Jamboree – 10th</title>
<link rel="stylesheet" href="https://fonts.googleapis.com/css2?family=Oswald:wght@500;600;700&family=Ultra&display=swap">
<style>
  :root {
    --frame-dark: #45282b;
    --cream: #fff8c9;
    --panel: #e7e3b5;
    --red: #d22b3c;
    --ink: #221816;
    --gold: #f2b705;
    --gold-shadow: #eebb00;
    --pig-pink: #f9dfc0;
    --denim: #7a98ae;
  }
  * { margin: 0; padding: 0; box-sizing: border-box; }
  html, body {
    width: 848px; height: 1200px; overflow: hidden;
    background: var(--frame-dark);
  }
  .poster { position: relative; width: 848px; height: 1200px; }
  .poster svg { position: absolute; inset: 0; }
  .display { font-family: "Ultra", "Rockwell Extra Bold", "Rockwell", serif; font-weight: 900; }
  .condensed { font-family: "Oswald", sans-serif; font-weight: 600; }
  .mascot {
    position: absolute; left: 40px; top: 118px; width: 322px; height: 392px;
    border-radius: 45% 45% 48% 48%;
    background: linear-gradient(180deg, var(--pig-pink) 0%, var(--pig-pink) 42%, var(--denim) 43%, var(--denim) 100%);
  }
</style>
</head>
<body>
<main class="poster">
  <svg width="848" height="1200" viewBox="0 0 848 1200">
    <!-- frame -->
    <rect class="frame-cream" x="13" y="13" width="822" height="1174" fill="var(--cream)"/>
    <rect class="field-red" x="34" y="34" width="780" height="1131" fill="var(--red)"/>

    <!-- slanted panel -->
    <polygon class="panel" points="52,519 795,287 795,1060 52,830"
      fill="var(--panel)" stroke="var(--cream)" stroke-width="7" stroke-linejoin="round"/>

    <!-- name bar -->
    <rect class="name-bar" x="51" y="48" width="449" height="89" fill="var(--ink)"/>
    <text class="condensed name-text" x="275" y="110" text-anchor="middle" font-size="40"
      fill="var(--cream)" textLength="420" lengthAdjust="spacingAndGlyphs">HARLAN RIDGE SMOKEHOUSE</text>

    <!-- anniversary badge -->
    <ellipse class="badge" cx="652" cy="183" rx="140" ry="104" fill="var(--gold)"
      stroke="var(--red)" stroke-width="1.5"/>
    <ellipse cx="652" cy="183" rx="136" ry="100" fill="none" stroke="var(--red)" stroke-width="1"/>
    <text class="display badge-number" x="556" y="235" font-size="140" fill="var(--ink)"
      stroke="var(--ink)" stroke-width="6" textLength="160" lengthAdjust="spacingAndGlyphs">10</text>
    <text class="display badge-suffix" x="720" y="148" font-size="24" fill="var(--ink)">TH</text>

    <!-- tagline -->
    <text class="condensed tagline" transform="translate(324,492) rotate(-18.3)" font-size="27"
      fill="var(--ink)" textLength="472" lengthAdjust="spacingAndGlyphs">BEERS, BANDS, BBQ + BOURBON!!</text>

    <!-- big BBQ -->
    <g class="display headline">
      <g fill="var(--gold-shadow)">
        <text x="76" y="817" font-size="320" textLength="112" lengthAdjust="spacingAndGlyphs">B</text>
        <text x="202" y="850" font-size="380" textLength="178" lengthAdjust="spacingAndGlyphs">B</text>
        <text x="405" y="905" font-size="600" textLength="370" lengthAdjust="spacingAndGlyphs">Q</text>
      </g>
      <g fill="var(--ink)" stroke="var(--ink)" stroke-width="10" stroke-linejoin="round">
        <text x="70" y="805" font-size="320" textLength="112" lengthAdjust="spacingAndGlyphs">B</text>
        <text x="196" y="836" font-size="380" textLength="178" lengthAdjust="spacingAndGlyphs">B</text>
        <text x="397" y="885" font-size="600" textLength="370" lengthAdjust="spacingAndGlyphs">Q</text>
      </g>
    </g>

    <!-- event word -->
    <text class="condensed event-word" transform="translate(86,962) skewY(17)" font-size="124"
      font-weight="700" fill="var(--cream)" textLength="610" lengthAdjust="spacingAndGlyphs">JAMBOREE</text>

    <!-- date diamond -->
    <polygon class="date-diamond" points="52,1089 218,1024 384,1089 218,1152" fill="var(--ink)"/>
    <polygon points="86,1089 218,1038 350,1089 218,1139" fill="none" stroke="var(--cream)" stroke-width="3"/>
    <text class="condensed date-text" x="218" y="1099" text-anchor="middle" font-size="28"
      fill="var(--cream)">SEPT 4+5, 2020</text>

    <!-- event details in bottom frame band -->
    <text class="condensed details" x="424" y="1181" text-anchor="middle" font-size="13"
      font-weight="500" fill="var(--ink)" textLength="800" lengthAdjust="spacingAndGlyphs">HOSTED BY COPPERFIELD HOLLOW DISTILLERY · 2817 MARLOW PIKE ASHBY, KY 40198 · $5 ADMISSION · FREE MUSIC · FREE PARKING</text>
  </svg>

  <div class="mascot" role="img" aria-label="Illustration of a cheerful cartoon pig in blue overalls standing on the panel"></div>
</main>
</body>
</html>
```